Northgate Prestige Academy needs a Courses Fine Brochure

An unique business school 100% focused on the luxury market that offers programs in NY, L.A., Miami, Paris, Milan, and São Paulo, needs a comprehensive brochure with all your programs.
In two versions, to print and as a web flipping book.
Please find attached two examples of our single program brochures.
PLEASE NOTE THAT ALL UPLOADED MATERIALS ARE SAMPLES OF WHAT WE ALREADY DID, AS SOON AS I´VE CHOSEN A DESIGNER I´LL SEND THE CORRECT FILES, TEXTS AND "SUGGESTED IMAGES".
Updates

Target Market(s)

US students interested in short term programs focused on luxury.
The brochure must display 12 short term programs that will take place in 2017 in Miami, Florida.

Industry/Entity Type

Education

Contact Information for Business Card

Black sober fine finishing business card.
Name, place, phone, address, e-mail, cel.

Font styles to use
Serif
Sans Serif
Script

Requirements
Must have
• Fine finishing, as smooth touch mate lamination, and/or hotstamping, and/or located varnish.
• Easy to read. Every program has Name, brief introduction, date, time, duration, some keynote speaker picture and brief resumé (short cv). And 5 to 10 content topics. Course highlights.
Nice to have
• Luxury products and services. Sofisticated images, closeups and nice views.
• We are talking about teaching luxury for entrepreneurs mainly.
• Business owners or high level executives.
Should not have
• Less is more. Promotional look. Cheap look. Colorful blasting design.

```html
<!DOCTYPE html>
<html lang="en">
<head>
<meta charset="utf-8">
<title>Northgate Prestige Academy – Luxury Programs Miami 2017</title>
<link href="https://fonts.googleapis.com/css2?family=Cinzel:wght@400;500&family=Cormorant+SC:wght@400;500&display=swap" rel="stylesheet">
<style>
:root{
  --stage:#2b241f;
  --ink:#141414;
  --panel:#1a1a1a;
  --panel-soft:#1e1e1e;
  --gold:#b8924f;
  --gold-dim:#7a6238;
  --white:#ecebe8;
  --grey:#9a9a9a;
  --faint:#2c2c2c;
}
*{margin:0;padding:0;box-sizing:border-box}
html,body{width:1200px;height:800px;overflow:hidden;background:var(--stage)}
body{position:relative;font-family:"Cinzel",serif;color:var(--white)}
.spread{position:absolute;left:124px;width:952px;height:240px;display:flex;box-shadow:0 6px 18px rgba(0,0,0,.5)}
.spread--outer{top:80px}
.spread--inner{top:356px}
.panel{position:relative;width:238px;height:240px;background:var(--panel);overflow:hidden}
.photo{position:absolute}
/* outer spread */
.panel--skyline .photo{inset:0;background:linear-gradient(180deg,#c9b8a4 0%,#a89482 35%,#5a5048 65%,#2a2420 100%)}
.back-contact{position:absolute;left:0;right:0;bottom:22px;text-align:center}
.brand-name{font-size:7px;color:var(--gold);letter-spacing:.6px}
.brand-tag{font-size:4.6px;color:var(--white);margin-top:6px;letter-spacing:.3px}
.contact-line{display:flex;justify-content:center;align-items:center;gap:10px;margin-top:14px;font-size:3.6px;color:var(--white)}
.contact-line .mark{display:inline-block;width:4px;height:4px;background:var(--gold);margin-right:2px;vertical-align:middle}
.cover-frame{position:absolute;left:14px;top:16px;bottom:16px;right:-2px;border-left:1px solid var(--gold-dim);border-bottom:1px solid var(--gold-dim)}
.cover-title{position:absolute;left:0;right:0;top:100px;text-align:center;color:var(--gold);line-height:1;font-weight:400}
.cover-title span{display:block}
.cover-title .l1,.cover-title .l2{font-size:13px;margin-bottom:1px}
.cover-title .l3{font-size:18px}
.cover-rule{width:14px;height:1px;background:var(--gold-dim);margin:0 auto 5px}
.cover-meta{position:absolute;left:0;right:0;top:160px;text-align:center;font-size:6px;line-height:1.4;color:var(--white)}
.collage{position:absolute;inset:0;display:grid;grid-template-columns:147px 91px;grid-template-rows:100px 52px 36px 52px;gap:1px;background:#111}
.collage .photo{position:relative}
.c1{background:linear-gradient(135deg,#5a4a7a,#c8c0d0 60%,#6a5a8a)}
.c2{background:linear-gradient(180deg,#8aa8c0,#c4b08a 70%,#5a7090)}
.c3{background:linear-gradient(180deg,#8a9aa8,#4a4a50)}
.c4{background:linear-gradient(180deg,#b8c8d8,#e8e8e8 60%,#7ab0c0)}
.c5{background:linear-gradient(180deg,#c8d8e0,#e0d8c8)}
.c6{background:linear-gradient(180deg,#6a90b8,#d8d0b8 70%,#8aa0a0)}
.c7{background:linear-gradient(135deg,#e8d8a0,#6a5a3a 70%,#2a2418)}
/* inner spread */
.panel--program .photo{left:0;top:0;width:238px;height:82px}
.p-restaurant{background:linear-gradient(180deg,#3a4050,#6a5a40 60%,#201a14)}
.p-hotel{background:linear-gradient(180deg,#1a2a4a,#4a4438 55%,#2a2620)}
.p-glasses{background:linear-gradient(135deg,#5a6aa0,#c8b0a0 45%,#6a2a24 80%)}
.photo-caption{position:absolute;right:8px;top:75px;font-size:3px;color:var(--white)}
.program-title{position:absolute;left:14px;top:95px;font-size:11px;color:var(--gold);white-space:nowrap;font-weight:400}
.program-title b{font-weight:400;color:var(--white);font-family:"Cormorant SC",serif;font-size:13px}
.program-sub{position:absolute;left:150px;top:112px;font-size:3px;color:var(--grey)}
.schedule{position:absolute;left:14px;top:120px;width:116px;list-style:none}
.schedule li{font-size:4.4px;line-height:1;margin-bottom:4px;white-space:nowrap}
.schedule .time{color:var(--gold);display:inline-block;width:15px;font-size:3px}
.schedule .who{display:block;margin-left:15px;font-size:2.8px;color:var(--gold-dim);margin-top:1.5px}
.talks{position:absolute;left:134px;top:120px;width:96px}
.talk{margin-bottom:8px}
.talk-head{font-size:3.4px;color:var(--gold)}
.talk-q{font-size:3.2px;color:var(--white);margin-top:2px;line-height:1.3}
.speaker{display:flex;gap:4px;margin-top:4px;align-items:flex-start}
.portrait{flex:none;width:18px;height:18px;border-radius:50%;background:radial-gradient(circle at 50% 40%,#cfcfcf,#777)}
.speaker-text{font-size:2.8px;line-height:1.35;color:var(--grey)}
.speaker-text .name{color:var(--gold-dim)}
.special{position:absolute;left:14px;bottom:14px;font-size:2.8px;color:var(--grey)}
.special p{font-size:4.2px;color:var(--white);margin-top:2px}
.special .time{color:var(--gold);font-size:3px;margin-right:4px}
.notes{position:absolute;left:134px;bottom:18px;font-size:2.4px;color:var(--grey);line-height:1.4}
.panel--closing{background:var(--panel-soft)}
.closing-title{position:absolute;left:0;right:0;top:104px;text-align:center;color:var(--faint);line-height:1}
.closing-title .l1,.closing-title .l2{display:block;font-size:13px;margin-bottom:1px}
.closing-title .l3{display:block;font-size:18px}
.closing-meta{position:absolute;left:0;right:0;top:150px;text-align:center;font-size:6px;color:var(--faint);line-height:1.4}
.palette{position:absolute;left:530px;top:669px;width:140px;height:54px}
</style>
</head>
<body>

<section class="spread spread--outer">
  <div class="panel panel--skyline">
    <div class="photo" role="img" aria-label="Miami skyline at dusk seen from a high rooftop"></div>
  </div>
  <div class="panel panel--back">
    <div class="back-contact">
      <div class="brand-name">Northgate Prestige Academy</div>
      <div class="brand-tag">Business School 100% Focused on Luxury</div>
      <div class="contact-line">
        <span>+1 305 555 0147 &nbsp;|&nbsp; www.northgateprestige.edu</span>
        <span><i class="mark"></i>/northgateacademy</span>
        <span><i class="mark"></i>/northgateluxury</span>
      </div>
    </div>
  </div>
  <div class="panel panel--cover">
    <div class="cover-frame"></div>
    <h1 class="cover-title">
      <span class="l1">Luxury</span>
      <span class="l2">Short Programs</span>
      <span class="l3">Miami 2017</span>
    </h1>
    <div class="cover-meta">
      <div class="cover-rule"></div>
      12 Programs · January to December 2017<br>Northgate Prestige Academy · Miami · Florida
    </div>
  </div>
  <div class="panel panel--gallery">
    <div class="collage">
      <div class="photo c1" role="img" aria-label="Luxury suite with purple curtains"></div>
      <div class="photo c2" role="img" aria-label="Oceanfront resort seen from above"></div>
      <div class="photo c3" role="img" aria-label="Historic boutique facade"></div>
      <div class="photo c4" role="img" aria-label="White residential tower with balconies" style="grid-row:2/4"></div>
      <div class="photo c5" role="img" aria-label="Lounge with sea view"></div>
      <div class="photo c6" role="img" aria-label="Miami beach with palm trees"></div>
      <div class="photo c7" role="img" aria-label="Sunlit corridor detail"></div>
    </div>
  </div>
</section>

<section class="spread spread--inner">
  <article class="panel panel--program">
    <div class="photo p-restaurant" role="img" aria-label="Fine dining room at night"></div>
    <span class="photo-caption">Coral Terrace Restaurant</span>
    <h2 class="program-title"><b>01–04</b> - Luxury Business</h2>
    <div class="program-sub">Programs 2017</div>
    <ul class="schedule">
      <li><span class="time">Jan</span>Luxury Brand Management<span class="who">Jan 16–20 · 9am–5pm · 5 days</span></li>
      <li><span class="time">Feb</span>The Luxury Entrepreneur<span class="who">Feb 13–17 · 9am–5pm · 5 days</span></li>
      <li><span class="time">Mar</span>Luxury Retail Excellence<span class="who">Mar 13–16 · 9am–5pm · 4 days</span></li>
      <li><span class="time">Apr</span>Luxury Finance &amp; Pricing<span class="who">Apr 10–13 · 9am–5pm · 4 days</span></li>
      <li><span class="time">·</span>Course Highlights<span class="who">Brand heritage · Pricing · Store visits</span></li>
      <li><span class="time">·</span>Who Should Attend<span class="who">Business owners · Senior executives</span></li>
    </ul>
    <div class="talks">
      <div class="talk">
        <div class="talk-head">Luxury Brand Management</div>
        <div class="talk-q">How is a timeless brand built? Heritage, rarity and desire in a new market.</div>
        <div class="speaker"><div class="portrait" role="img" aria-label="Keynote speaker portrait"></div>
          <div class="speaker-text"><span class="name">Keynote · Brand Director</span><br>Twenty years leading fashion and jewelry houses in Paris and New York.</div></div>
      </div>
      <div class="talk">
        <div class="talk-head">The Luxury Entrepreneur</div>
        <div class="talk-q">From idea to maison: how to launch and grow a premium business.</div>
        <div class="speaker"><div class="portrait" role="img" aria-label="Keynote speaker portrait"></div>
          <div class="speaker-text"><span class="name">Keynote · Founder</span><br>Founder of three luxury ventures, mentor to young brands in Miami.</div></div>
      </div>
    </div>
    <div class="special">Special Program<p><span class="time">20:00</span>Welcome Dinner at Coral Terrace Restaurant</p></div>
    <div class="notes">* Programs subject to change.<br>* Certificate of completion.</div>
  </article>

  <article class="panel panel--program">
    <div class="photo p-hotel" role="img" aria-label="Illuminated hotel building at dusk"></div>
    <span class="photo-caption" style="right:auto;left:16px">Bayview Grand Hotel</span>
    <h2 class="program-title"><b>05–08</b> - Luxury Marketing</h2>
    <div class="program-sub">Programs 2017</div>
    <ul class="schedule">
      <li><span class="time">May</span>Luxury Marketing Strategy<span class="who">May 15–19 · 9am–5pm · 5 days</span></li>
      <li><span class="time">Jun</span>Digital Luxury &amp; Social Media<span class="who">Jun 12–15 · 9am–5pm · 4 days</span></li>
      <li><span class="time">Jul</span>Clienteling &amp; Client Experience<span class="who">Jul 17–20 · 9am–5pm · 4 days</span></li>
      <li><span class="time">Aug</span>Luxury Events &amp; PR<span class="who">Aug 14–17 · 9am–5pm · 4 days</span></li>
      <li><span class="time">·</span>Course Highlights<span class="who">Storytelling · Digital · Case studies</span></li>
      <li><span class="time">·</span>Who Should Attend<span class="who">Marketing heads · Brand owners</span></li>
    </ul>
    <div class="talks">
      <div class="talk">
        <div class="talk-head">Luxury Marketing Strategy</div>
        <div class="talk-q">Selling dreams, not products: the art of communicating exclusivity.</div>
        <div class="speaker"><div class="portrait" role="img" aria-label="Keynote speaker portrait"></div>
          <div class="speaker-text"><span class="name">Keynote · Marketing Officer</span><br>Led global campaigns for watch and leather goods houses.</div></div>
      </div>
      <div class="talk">
        <div class="talk-head">Digital Luxury &amp; Social Media</div>
        <div class="talk-q">How to stay rare online? Integration, personalization and innovation.</div>
        <div class="speaker"><div class="portrait" role="img" aria-label="Keynote speaker portrait"></div>
          <div class="speaker-text"><span class="name">Keynote · Digital Director</span><br>Heads e-commerce for a premium group across the Americas.</div></div>
      </div>
    </div>
    <div class="special">Special Program<p><span class="time">Evening</span>Discovering Miami (a design journey<br>through the city)</p></div>
    <div class="notes">* Programs subject to change.<br>* Certificate of completion.</div>
  </article>

  <article class="panel panel--program">
    <div class="photo p-glasses" role="img" aria-label="Wine glasses raised at a cocktail party"></div>
    <span class="photo-caption">Cocktail Party at Bayview Grand Hotel</span>
    <h2 class="program-title"><b>09–12</b> - Luxury Experience</h2>
    <div class="program-sub">Programs 2017</div>
    <ul class="schedule">
      <li><span class="time">Sep</span>Luxury Hospitality<span class="who">Sep 11–15 · 9am–5pm · 5 days</span></li>
      <li><span class="time">Oct</span>Fine Wines &amp; Gastronomy<span class="who">Oct 16–19 · 9am–5pm · 4 days</span></li>
      <li><span class="time">Nov</span>Luxury Real Estate &amp; Yachting<span class="who">Nov 13–16 · 9am–5pm · 4 days</span></li>
      <li><span class="time">Dec</span>Jewelry &amp; Watches<span class="who">Dec 4–7 · 9am–5pm · 4 days</span></li>
      <li><span class="time">·</span>Course Highlights<span class="who">Service codes · Tastings · Site visits</span></li>
      <li><span class="time">·</span>Who Should Attend<span class="who">Entrepreneurs · High level executives</span></li>
    </ul>
    <div class="talks">
      <div class="talk">
        <div class="talk-head">Luxury Hospitality</div>
        <div class="talk-q">Delivering service as promised: the art of enchanting the guest.</div>
        <div class="speaker"><div class="portrait" role="img" aria-label="Keynote speaker portrait"></div>
          <div class="speaker-text"><span class="name">Keynote · General Manager</span><br>Opened five-star resorts in Miami, Dubai and the Caribbean.</div></div>
      </div>
      <div class="talk">
        <div class="talk-head">Fine Wines &amp; Gastronomy</div>
        <div class="talk-q">What makes a table unforgettable? A real case study.</div>
        <div class="speaker"><div class="portrait" role="img" aria-label="Keynote speaker portrait"></div>
          <div class="speaker-text"><span class="name">Keynote · Master Sommelier</span><br>Curates cellars for leading restaurants in the United States.</div></div>
      </div>
    </div>
    <div class="special">Special Program<p>Cocktail Party at Bayview Grand Hotel</p></div>
    <div class="notes">* Programs subject to change.<br>* Certificate of completion.</div>
  </article>

  <aside class="panel panel--closing">
    <div class="closing-title">
      <span class="l1">Luxury</span>
      <span class="l2">Short Programs</span>
      <span class="l3">Miami 2017</span>
    </div>
    <div class="closing-meta">12 Programs · January to December 2017<br>Northgate Prestige Academy · Miami · Florida</div>
  </aside>
</section>

<svg class="palette" viewBox="0 0 140 54" aria-label="Colour palette">
  <circle cx="27" cy="27" r="26.5" fill="var(--ink)"/>
  <circle cx="67" cy="27" r="26.5" fill="var(--gold)"/>
  <circle cx="107" cy="27" r="26.5" fill="#ffffff"/>
</svg>

</body>
</html>
```